Dokumentationsmappe gesucht
Zielgruppe
Jedes mittelständische, deutsche Unternehmen verbraucht in irgendeiner Form Energie, meistens in Form von Strom und/oder Gas. Meistens hat man als Unternehmer keine Zeit sich über das Ener­gie­spa­ren Gedanken zu machen und das obwohl man mit den richtigen Maßnahmen seinen Verbrauch um bis zu 25% reduzieren kann. Ein um 25% reduzierter Verbrauch würde auch auf der Energierechnung 25% sparen.
Das weiß auch der deutsche Staat, der jedes Jahr Investments in Milliarden Höhe tätigt, um seine Klimaziele zu erreichen. Unter anderem werden vom Bundesstelle für Gewerbe und Handelsaufsicht Energieberatungen subventioniert. Deutsche, mittelständische Unternehmen wird so die Möglichkeit geboten, komplett kostenneutral ihren Teil zum Umweltschutz beizutragen. Der positive Nebeneffekt, man spart sich jedes Jahr noch bares Geld, da aus einem geminderten Verbrauch auch eine kleinere Energie Rechnung resultiert.
KLV hilft Unternehmen sich alle Subventionierungen zu sichern. Wir schicken einen vom Staat zertifizierten Ingenieur im Unternehmen vorbei, der eine für den Unternehmer kostenneutrale Energieberatung durchführt. Der Ingenieur ist auf die Energiebranche spezialisiert und wird deshalb schnell erkennen, wo Energie eingespart werden kann.
Aufgabenstellung
Wir benötigen eine Dokumentationsmappe, die sich an der Seite www.klv-sparwerk.de anlehnt und die dem Unternehmer mit dem Inhalt des 'Auftrages zum Energieaudit' überlassen wird. Es dient somit auch als Verkaufshilfe bei Terminen am Kunden.

```html
<!DOCTYPE html>
<html lang="de">
<head>
<meta charset="utf-8">
<title>KLV Dokumentationsmappe</title>
<link rel="stylesheet" href="https://fonts.googleapis.com/css2?family=Saira+Semi+Condensed:wght@400;500;700&display=swap">
<style>
  :root {
    --bg: #cfe4f2;
    --paper: #f6f6f6;
    --band-light: #efefef;
    --band-mid: #e9e9e9;
    --band-dark: #dedede;
    --accent: #3f9ae0;
    --text: #6d6d6d;
    --logo: #8a8a8a;
    --illustration: #e4e4e4;
    --badge: #d9a93a;
  }
  * { margin: 0; padding: 0; box-sizing: border-box; }
  html, body { width: 1200px; height: 816px; overflow: hidden; }
  body {
    background: var(--bg);
    font-family: "Saira Semi Condensed", sans-serif;
    color: var(--text);
    position: relative;
  }
  .cover {
    position: absolute;
    left: 325px; top: 20px;
    width: 550px; height: 776px;
    background: var(--paper);
    border-top: 4px solid var(--accent);
    box-shadow: 0 4px 14px rgba(40, 80, 110, 0.18);
    overflow: hidden;
  }
  .brand {
    position: absolute;
    left: 39px; top: 36px;
    font-size: 44px; font-weight: 700;
    letter-spacing: -1px;
    color: var(--logo);
    line-height: 1;
  }
  .hero-illustration {
    position: absolute;
    left: 174px; top: 101px;
    width: 196px; height: 294px;
    background: linear-gradient(180deg, #ececec, var(--illustration));
    border-radius: 4px;
  }
  .partner-badge {
    position: absolute;
    left: 464px; top: 376px;
    width: 61px; height: 43px;
    background: var(--badge);
    border-radius: 2px;
  }
  .benefits {
    position: absolute;
    left: 0; top: 445px;
    width: 100%; height: 91px;
    background: var(--band-light);
  }
  .benefit {
    position: absolute;
    top: 14px;
    width: 110px;
    margin-left: -55px;
    text-align: center;
  }
  .benefit svg { display: block; margin: 0 auto; width: 36px; height: 36px; }
  .benefit-label {
    margin-top: 8px;
    font-size: 9px;
    letter-spacing: 0.6px;
    line-height: 11px;
  }
  .claim {
    position: absolute;
    left: 0; top: 536px;
    width: 100%; height: 168px;
    background: var(--band-mid);
    text-align: center;
  }
  .claim-title {
    margin-top: 32px;
    font-size: 26px; font-weight: 500;
    letter-spacing: 2.4px;
    color: #6a6a6a;
  }
  .claim-text {
    margin-top: 24px;
    font-size: 10.5px;
    letter-spacing: 0.8px;
    line-height: 12px;
  }
  .contact {
    position: absolute;
    left: 0; top: 704px;
    width: 100%; height: 72px;
    background: var(--band-dark);
    text-align: center;
    font-size: 10.5px;
    letter-spacing: 0.9px;
    line-height: 14px;
    padding-top: 24px;
  }
</style>
</head>
<body>
  <main class="cover">
    <div class="brand">KLV</div>

    <div class="hero-illustration" role="img" aria-label="Strichzeichnung: Mann schüttet Geldscheine aus einem Papierstapel"></div>
    <div class="partner-badge" role="img" aria-label="Kampagnen-Siegel"></div>

    <section class="benefits">
      <div class="benefit" style="left:99px">
        <svg viewBox="0 0 36 36" aria-hidden="true">
          <path d="M25 8 A11 11 0 1 0 25 28" fill="none" stroke="var(--accent)" stroke-width="4"/>
          <rect x="6" y="13" width="16" height="3" fill="var(--accent)"/>
          <rect x="6" y="19" width="16" height="3" fill="var(--accent)"/>
        </svg>
        <div class="benefit-label">Kostenneutrale<br>Beratung</div>
      </div>
      <div class="benefit" style="left:215px">
        <svg viewBox="0 0 36 36" aria-hidden="true">
          <rect x="4" y="7" width="28" height="26" rx="2" fill="none" stroke="var(--accent)" stroke-width="2.5"/>
          <rect x="4" y="7" width="28" height="6" fill="var(--accent)"/>
          <rect x="10" y="3" width="3" height="7" fill="var(--accent)"/>
          <rect x="23" y="3" width="3" height="7" fill="var(--accent)"/>
          <path d="M4 19H32M4 25H32M11 13V33M18 13V33M25 13V33" stroke="var(--accent)" stroke-width="1.5"/>
        </svg>
        <div class="benefit-label">Gesicherte<br>Fördermittel</div>
      </div>
      <div class="benefit" style="left:329px">
        <svg viewBox="0 0 36 36" aria-hidden="true">
          <path d="M18 4a10 10 0 0 0-6 18v4h12v-4a10 10 0 0 0-6-18z" fill="none" stroke="var(--accent)" stroke-width="2.8"/>
          <rect x="13" y="28" width="10" height="2.5" fill="var(--accent)"/>
          <rect x="14.5" y="32" width="7" height="2.5" fill="var(--accent)"/>
        </svg>
        <div class="benefit-label">Bis 25% Energie &amp;<br>Kosten einsparen</div>
      </div>
      <div class="benefit" style="left:436px">
        <svg viewBox="0 0 36 36" aria-hidden="true">
          <circle cx="16" cy="10" r="7" fill="var(--accent)"/>
          <path d="M3 30c0-8 6-12 13-12s9 2 11 4l-7 8z" fill="var(--accent)"/>
          <path d="M20 27l5 5 9-10" fill="none" stroke="var(--accent)" stroke-width="3"/>
        </svg>
        <div class="benefit-label">Experten gesicherte<br>Durchführung</div>
      </div>
    </section>

    <section class="claim">
      <h1 class="claim-title">Energie sparen heißt Geld sparen!</h1>
      <p class="claim-text">Hier ist Ihre kostenneutrale Energieberatung.<br>Lassen Sie sich von Anfang an von Experten begleiten<br>und sparen Sie ab sofort Energie und damit bares Geld!</p>
    </section>

    <footer class="contact">
      KLV GmbH | Lindenhofweg 14 | 54321 Feldau<br>
      kontakt@klv-sparwerk.de | +49 1234 5678900
    </footer>
  </main>
</body>
</html>
```